Social Media Overlay for Ormond Real Estate

We need an social media overlay that can be added to a photo of a house that includes our current logo and a call to action of "Just Listed". This needs to be something that we can use for every new house that we list. Attached is our current logo in both company colors, purple and white. An example of a overlay from Plazeo that we like.

Target Market(s)

Social Media Real Estate Community - Real Estate Agents, Brokers, Buyers & Sellers

Industry/Entity Type

Real Estate

Font styles to use
Sans Serif

Colors
6c459b

Requirements
Must have
• the company colors, purple and white and the company logo
Nice to have
• call to action "Just Listed"
• some layered, texture, or 3-D effect
Should not have
• Should be clean and simple; nothing too busy

```html
<!DOCTYPE html>
<html lang="en">
<head>
<meta charset="utf-8">
<title>Ormond Real Estate – Just Listed Overlays</title>
<link href="https://fonts.googleapis.com/css2?family=Anton&family=Quicksand:wght@600&family=Raleway:wght@400&display=swap" rel="stylesheet">
<style>
  :root {
    --board: #5b5d61;
    --brand-purple: #6c459b;
    --deep-purple: #3c0a6b;
    --royal-purple: #5e2a8c;
    --magenta: #c400d8;
    --violet: #9a00d6;
    --badge-dark: #2a1f2d;
    --white: #ffffff;
    --silver-light: #f2f2f4;
    --silver-dark: #9a9aa2;
    --label: #f4f4f6;
  }
  * { margin: 0; padding: 0; box-sizing: border-box; }
  html, body {
    width: 1200px; height: 2319px; overflow: hidden;
    background: var(--board);
  }
  .board { position: relative; width: 1200px; height: 2319px; }
  .sample-label {
    position: absolute; left: 0; width: 1200px; text-align: center;
    font-family: "Raleway", sans-serif; font-weight: 400;
    font-size: 37px; color: var(--label); letter-spacing: 0.5px;
  }
  .overlay-card {
    position: absolute; left: 114px; width: 972px; height: 639px;
    box-shadow: 0 14px 18px rgba(0,0,0,0.35);
    overflow: hidden;
  }
  .overlay-card svg { display: block; width: 100%; height: 100%; }
  .cta { font-family: "Anton", sans-serif; text-anchor: middle; }
  .brand { font-family: "Quicksand", sans-serif; font-weight: 600; text-anchor: middle; }
</style>
</head>
<body>
<main class="board">

  <p class="sample-label" style="top:62px">SAMPLE- 1</p>
  <section class="overlay-card" style="top:125px">
    <svg viewBox="0 0 1080 710" xmlns="http://www.w3.org/2000/svg">
      <defs>
        <linearGradient id="photo-house-a" x1="0" y1="0" x2="0" y2="1">
          <stop offset="0" stop-color="#f1ece6"/>
          <stop offset="0.35" stop-color="#c9ab98"/>
          <stop offset="0.7" stop-color="#8a7b5a"/>
          <stop offset="1" stop-color="#5f7d3c"/>
        </linearGradient>
        <linearGradient id="purple-sweep" x1="0" y1="0" x2="1" y2="1">
          <stop offset="0" stop-color="#4a0a86"/>
          <stop offset="0.55" stop-color="#7a12b8"/>
          <stop offset="1" stop-color="#2c0656"/>
        </linearGradient>
        <linearGradient id="silver" x1="0" y1="0" x2="1" y2="0">
          <stop offset="0" stop-color="var(--silver-dark)"/>
          <stop offset="0.5" stop-color="var(--silver-light)"/>
          <stop offset="1" stop-color="var(--silver-dark)"/>
        </linearGradient>
      </defs>
      <rect role="img" aria-label="Photo of a two-storey brick house with garage, trees and fence" width="1080" height="710" fill="url(#photo-house-a)"/>
      <polygon points="0,385 400,525 700,500 1080,330 1080,375 700,535 400,560 0,425" fill="url(#silver)"/>
      <polygon points="0,420 400,560 700,535 1080,372 1080,710 0,710" fill="url(#purple-sweep)"/>
      <circle cx="540" cy="482" r="160" fill="var(--white)"/>
      <text class="cta" x="540" y="468" font-size="68" fill="var(--royal-purple)">JUST</text>
      <text class="cta" x="540" y="550" font-size="68" fill="var(--royal-purple)">LISTED !</text>
      <text class="brand" x="900" y="615" font-size="62" fill="var(--white)">Ormond</text>
      <text class="brand" x="900" y="665" font-size="40" fill="var(--white)">Real Estate</text>
    </svg>
  </section>

  <p class="sample-label" style="top:786px">SAMPLE- 2</p>
  <section class="overlay-card" style="top:848px">
    <svg viewBox="0 0 1080 710" xmlns="http://www.w3.org/2000/svg">
      <defs>
        <linearGradient id="photo-house-b" x1="0" y1="0" x2="0" y2="1">
          <stop offset="0" stop-color="#ece6df"/>
          <stop offset="0.4" stop-color="#c6a790"/>
          <stop offset="0.75" stop-color="#8c7a58"/>
          <stop offset="1" stop-color="#56783a"/>
        </linearGradient>
        <linearGradient id="magenta-base" x1="0" y1="0" x2="1" y2="0">
          <stop offset="0" stop-color="var(--magenta)"/>
          <stop offset="0.5" stop-color="#b000e0"/>
          <stop offset="1" stop-color="var(--violet)"/>
        </linearGradient>
        <linearGradient id="silver-ring" x1="0" y1="0" x2="1" y2="1">
          <stop offset="0" stop-color="var(--silver-light)"/>
          <stop offset="0.5" stop-color="var(--silver-dark)"/>
          <stop offset="1" stop-color="var(--silver-light)"/>
        </linearGradient>
      </defs>
      <rect width="1080" height="710" fill="var(--white)"/>
      <rect width="535" height="28" fill="var(--magenta)"/>
      <rect y="0" width="28" height="710" fill="var(--magenta)"/>
      <rect x="1052" y="420" width="28" height="290" fill="var(--violet)"/>
      <rect y="595" width="1080" height="115" fill="url(#magenta-base)"/>
      <rect role="img" aria-label="Photo of a two-storey brick house with lawn and flower beds" x="28" y="28" width="1024" height="557" fill="url(#photo-house-b)" stroke="#9bb02e" stroke-width="2"/>
      <polygon points="730,28 1052,28 1052,220" fill="var(--white)" opacity="0.75"/>
      <text class="brand" x="970" y="94" font-size="38" fill="var(--royal-purple)">Ormond</text>
      <text class="brand" x="970" y="121" font-size="24" fill="var(--royal-purple)">Real Estate</text>
      <circle cx="853" cy="535" r="158" fill="url(#silver-ring)"/>
      <circle cx="853" cy="535" r="136" fill="var(--royal-purple)"/>
      <text class="cta" x="853" y="522" font-size="66" fill="var(--white)">JUST</text>
      <text class="cta" x="853" y="598" font-size="66" fill="var(--white)">LISTED !</text>
    </svg>
  </section>

  <p class="sample-label" style="top:1511px">SAMPLE- 3</p>
  <section class="overlay-card" style="top:1571px">
    <svg viewBox="0 0 1080 710" xmlns="http://www.w3.org/2000/svg">
      <defs>
        <linearGradient id="photo-cottage" x1="0" y1="0" x2="0" y2="1">
          <stop offset="0" stop-color="#8fb0d6"/>
          <stop offset="0.3" stop-color="#dfe3e6"/>
          <stop offset="0.55" stop-color="#8a9a6a"/>
          <stop offset="1" stop-color="#9aa860"/>
        </linearGradient>
        <linearGradient id="soft-panel" x1="0" y1="0" x2="1" y2="1">
          <stop offset="0" stop-color="#ffffff"/>
          <stop offset="1" stop-color="#e6def0"/>
        </linearGradient>
        <linearGradient id="purple-panel" x1="0" y1="0" x2="1" y2="1">
          <stop offset="0" stop-color="#7a3aae"/>
          <stop offset="1" stop-color="#561f8e"/>
        </linearGradient>
        <linearGradient id="photo-interior" x1="0" y1="0" x2="1" y2="1">
          <stop offset="0" stop-color="#d8d2c8"/>
          <stop offset="1" stop-color="#6d6256"/>
        </linearGradient>
        <linearGradient id="photo-estate" x1="0" y1="0" x2="0" y2="1">
          <stop offset="0" stop-color="#c9d6e0"/>
          <stop offset="0.5" stop-color="#8a5a3a"/>
          <stop offset="1" stop-color="#4f7a2e"/>
        </linearGradient>
      </defs>
      <rect width="1080" height="710" fill="url(#soft-panel)"/>
      <rect role="img" aria-label="Photo of a small white cottage with a front lawn" width="540" height="710" fill="url(#photo-cottage)"/>
      <polygon points="513,0 1080,0 1080,135 983,227 640,60" fill="url(#purple-panel)"/>
      <polygon points="0,485 138,395 713,710 0,710" fill="url(#purple-panel)" stroke="var(--white)" stroke-width="12"/>
      <g transform="translate(613 155) rotate(24)">
        <rect x="-148" y="-88" width="296" height="176" fill="var(--white)"/>
        <rect role="img" aria-label="Photo of a bright living room" x="-136" y="-76" width="272" height="152" fill="url(#photo-interior)"/>
      </g>
      <g transform="translate(563 290) rotate(8)">
        <rect x="-135" y="-90" width="270" height="180" fill="var(--white)"/>
        <rect role="img" aria-label="Photo of a dining area and kitchen" x="-123" y="-78" width="246" height="156" fill="url(#photo-interior)"/>
      </g>
      <g transform="translate(543 505) rotate(22)">
        <rect x="-140" y="-100" width="280" height="200" fill="var(--white)"/>
        <rect role="img" aria-label="Photo of a large brick home with a garden path" x="-128" y="-88" width="256" height="176" fill="url(#photo-estate)"/>
      </g>
      <text class="brand" x="930" y="93" font-size="64" fill="var(--white)">Ormond</text>
      <text class="brand" x="930" y="128" font-size="34" fill="var(--white)">Real Estate</text>
      <circle cx="888" cy="517" r="147" fill="var(--badge-dark)"/>
      <text class="cta" x="888" y="505" font-size="66" fill="var(--white)">JUST</text>
      <text class="cta" x="888" y="582" font-size="66" fill="var(--white)">LISTED !</text>
    </svg>
  </section>

</main>
</body>
</html>
```